Personal training poster - 1200X900mm

Poster to promote my new personal training service at my gym. The poster will be printed and put into an aframe to be seen by people walking past my gym. It needs to be simple and eye catching with the text i have put in the must haves. The text and image should be the prominent parts of the design.

Target Market(s)

30-50 year old females

Industry/Entity Type

Fitness

Font styles to use
Sans Serif

Requirements
Must have
• my logo
• exercise graphic
• Must include the following text:
• Are you looking for a personal trainer? Our expert trainers can help you achieve you take your health and fitness back!
• Contact details:
• 1300452908
• info@brightmotiongym.example.com.au
• Located under the Harbourside Club

```html
<!DOCTYPE html>
<html lang="en">
<head>
<meta charset="utf-8">
<title>Personal Training Poster</title>
<link href="https://fonts.googleapis.com/css2?family=Bebas+Neue&family=Roboto:wght@400&display=swap" rel="stylesheet">
<style>
  :root {
    --page: #ffffff;
    --navy: #0f1f4f;
    --navy-deep: #0b1840;
    --accent-blue: #1d57c9;
    --yellow: #fdc12e;
    --yellow-light: #ffe13a;
    --cyan: #14b8d8;
    --white: #ffffff;
    --photo-dark: #1b1b1f;
    --photo-skin: #c7926d;
  }
  * { margin: 0; padding: 0; box-sizing: border-box; }
  html, body {
    width: 1200px; height: 936px; overflow: hidden;
    background: var(--page);
  }
  .canvas { position: relative; width: 1200px; height: 936px; }
  .poster {
    position: absolute; left: 263px; top: 18px;
    width: 779px; height: 1039px;
    transform: scale(0.866); transform-origin: 0 0;
    background: var(--navy);
    overflow: hidden;
  }
  .poster-shapes { position: absolute; inset: 0; width: 779px; height: 1039px; }
  .trainer-photo {
    position: absolute; left: 48px; top: 36px; width: 372px; height: 480px;
    background: linear-gradient(160deg, var(--photo-skin) 0%, var(--photo-dark) 45%, var(--photo-dark) 85%, var(--photo-skin) 100%);
    border-radius: 140px 140px 20px 60px;
  }
  .brand {
    position: absolute; left: 420px; top: 250px; width: 320px;
    text-align: center;
  }
  .brand-dot {
    width: 110px; height: 110px; border-radius: 50%;
    background: var(--accent-blue); margin: 0 auto 18px;
  }
  .brand-name {
    font-family: "Bebas Neue", sans-serif; font-size: 44px;
    letter-spacing: 3px; color: var(--yellow); line-height: 1;
  }
  .headline {
    position: absolute; left: 50px; top: 548px;
    font-family: "Bebas Neue", sans-serif; line-height: 1; letter-spacing: -1px;
  }
  .headline-lead { display: block; font-size: 80px; color: var(--cyan); }
  .headline-main { display: block; font-size: 86px; color: var(--yellow); margin-top: -2px; }
  .intro {
    position: absolute; left: 54px; top: 722px; width: 620px;
    font-family: "Roboto", sans-serif; font-size: 27px; line-height: 39px;
    color: var(--white);
  }
  .contacts { position: absolute; left: 54px; top: 826px; list-style: none; }
  .contact {
    display: flex; align-items: center; height: 66px;
    font-family: "Roboto", sans-serif; font-size: 28px; color: var(--white);
  }
  .contact-icon { width: 44px; height: 40px; margin-right: 20px; flex: none; }
</style>
</head>
<body>
<div class="canvas">
  <div class="poster">
    <svg class="poster-shapes" viewBox="0 0 779 1039" aria-hidden="true">
      <polygon points="0,0 640,0 0,452" fill="var(--yellow)"/>
      <polygon points="150,30 330,320 60,520" fill="var(--yellow-light)"/>
      <polygon points="20,470 330,320 140,560" fill="var(--accent-blue)" opacity="0.35"/>
      <polygon points="590,560 779,690 779,1039 660,1039" fill="var(--accent-blue)" opacity="0.55"/>
      <polygon points="640,700 779,760 779,1039 700,1039" fill="var(--accent-blue)" opacity="0.5"/>
    </svg>

    <div class="trainer-photo" role="img" aria-label="Photo of a woman in black activewear doing a seated twisting stretch"></div>

    <div class="brand">
      <div class="brand-dot"></div>
      <div class="brand-name">Bright Motion Gym</div>
    </div>

    <h1 class="headline">
      <span class="headline-lead">Are you looking for a</span>
      <span class="headline-main">Personal Trainer?</span>
    </h1>

    <p class="intro">Our expert trainers can help you achieve you take your health and fitness back!</p>

    <ul class="contacts">
      <li class="contact">
        <svg class="contact-icon" viewBox="0 0 44 40" aria-hidden="true">
          <path d="M8 4 L15 4 L18 13 L13 17 Q18 26 26 30 L30 25 L39 28 L39 35 Q38 39 33 39 Q14 36 5 12 Q4 5 8 4 Z" fill="var(--cyan)"/>
          <path d="M24 6 Q34 7 36 17" stroke="var(--yellow)" stroke-width="3" fill="none"/>
          <path d="M24 12 Q29 13 30 18" stroke="var(--yellow)" stroke-width="3" fill="none"/>
        </svg>
        <span>1300452908</span>
      </li>
      <li class="contact">
        <svg class="contact-icon" viewBox="0 0 44 40" aria-hidden="true">
          <rect x="1" y="7" width="42" height="27" fill="var(--cyan)"/>
          <path d="M1 7 L22 24 L43 7" stroke="var(--navy)" stroke-width="3" fill="none"/>
        </svg>
        <span>info@brightmotiongym.example.com.au</span>
      </li>
      <li class="contact">
        <svg class="contact-icon" viewBox="0 0 44 40" aria-hidden="true">
          <path d="M22 39 Q8 22 8 15 A14 14 0 0 1 36 15 Q36 22 22 39 Z" fill="var(--cyan)"/>
          <circle cx="22" cy="15" r="5" fill="var(--yellow)"/>
        </svg>
        <span>Located under the Harbourside Club</span>
      </li>
    </ul>
  </div>
</div>
</body>
</html>
```